Educational Agency in Abu Dhabi looking for an 8 pages website

We are looking for an 8 pages design for a website, we already have one but we need to refine it and it is www.brightcampuslink.ae - Please base it on logo colours (attached) I have uploaded our logo, website content logo colors to use it for the scheme.
We are looking for a smooth look and content added if possible, I also attached content and logo

Industry/Entity Type

Education

Coding

Coded - Design and coding required

Number of Pages Required

5+ page

```html
<!DOCTYPE html>
<html lang="en">
<head>
<meta charset="utf-8">
<title>Bright Campus — Educational Consulting</title>
<link rel="stylesheet" href="https://fonts.googleapis.com/css2?family=Lato:wght@300;400;700&family=Merriweather:wght@300;400&display=swap">
<style>
:root{
  --navy:#1d2b5e;
  --navy-dark:#16224b;
  --green:#a8cf3a;
  --ink:#333a45;
  --muted:#6b7280;
  --card:#f2f2f2;
  --line:#c9cdd6;
  --footer-bottom:#2b2b2b;
  --white:#ffffff;
  --star:#e6b422;
}
*{box-sizing:border-box;margin:0;padding:0}
html,body{width:1200px;height:4358px;overflow:hidden}
body{position:relative;background:var(--white);font-family:'Lato',sans-serif;color:var(--ink)}
.abs{position:absolute}
.site-header{left:0;top:0;width:1200px;height:128px;background:var(--navy)}
.brand{left:64px;top:0;width:122px;height:128px;background:var(--white);display:flex;flex-direction:column;align-items:center;justify-content:center;gap:8px}
.brand-mark{width:26px;height:26px;background:var(--navy);border-radius:50%}
.brand-name{font-weight:700;font-size:13px;color:var(--navy);letter-spacing:.5px;white-space:nowrap}
.util-nav{right:64px;top:10px;display:flex;gap:22px;font-size:13px;color:var(--white);align-items:center}
.util-nav .login{margin-right:14px}
.main-nav{left:405px;top:74px;display:flex;gap:32px;font-size:13px;color:var(--white);font-weight:700;letter-spacing:.4px}
.search{left:990px;top:64px;width:143px;height:38px;background:var(--white);border-radius:4px;font-size:13px;color:#999;padding:11px 12px}
.hero{left:0;top:128px;width:1200px;height:502px;background:linear-gradient(90deg,#eceff1 0%,#dde1e4 45%,#8f8a84 70%,#5b524b 100%)}
.hero h1{left:70px;top:110px;font-weight:300;font-size:46px;line-height:50px;color:#2a2f3a}
.hero h1 strong{font-weight:400;display:block}
.hero p{left:78px;top:238px;width:440px;font-size:16px;line-height:25px;color:#4a4f58}
.btn{display:flex;align-items:center;justify-content:center;font-size:15px}
.btn-green{background:var(--green);color:var(--white);border-radius:25px}
.btn-navy{background:var(--navy);color:var(--white);font-weight:700;letter-spacing:.5px}
.section-title{width:1200px;left:0;text-align:center;font-weight:300;font-size:40px;color:#3a3f4a}
.title-rule{left:560px;width:80px;height:2px;background:var(--line)}
.who-text{left:186px;top:790px;width:830px;text-align:center;font-size:13.5px;line-height:29px;color:#4a4f58}
.dest-card{width:242px;height:300px;background:var(--card);display:flex;flex-direction:column;align-items:center;padding-top:36px}
.dest-icon{width:76px;height:76px;border-radius:50%;background:#e2e4ea;border:2px solid #c8ccd8}
.dest-card h3{margin-top:22px;font-size:16px;font-weight:700;color:#2a2f3a}
.dest-card p{margin-top:10px;width:180px;text-align:center;font-size:12.5px;line-height:17px;color:#5a5f6a}
.dest-card .btn{margin-top:18px;width:137px;height:38px;font-size:13px;font-weight:400;letter-spacing:0}
.why-photo{left:0;top:1984px;width:616px;height:523px;background:linear-gradient(160deg,#c7c3bd 0%,#e0cba3 40%,#7b5a45 75%,#3c2f2b 100%)}
.why-panel{left:616px;top:1984px;width:584px;height:523px;background:var(--navy)}
.why-panel h2{position:absolute;left:84px;top:76px;font-family:'Merriweather',serif;font-weight:400;font-size:36px;color:var(--white)}
.why-list{position:absolute;left:84px;top:146px;width:440px;list-style:none}
.why-list li{display:flex;gap:24px;font-size:15px;line-height:23px;color:#e3e6ef;margin-bottom:22px}
.why-list svg{flex:none;margin-top:2px}
.serif-title{font-family:'Merriweather',serif;font-weight:300;font-size:32px;color:#2a2f3a}
.apply-text{left:195px;top:2680px;width:810px;text-align:center;font-size:19px;line-height:32px;color:#4a4f58}
.review{width:296px;height:334px;background:var(--white);border-top:3px solid var(--navy);box-shadow:0 4px 14px rgba(0,0,0,.12);text-align:center}
.avatar{position:absolute;left:93px;top:-60px;width:110px;height:110px;border-radius:50%;border:5px solid var(--white);box-shadow:0 2px 8px rgba(0,0,0,.15)}
.review h4{margin-top:88px;font-family:'Merriweather',serif;font-weight:400;font-size:19px;color:#2a2f3a}
.review .role{margin-top:8px;font-size:14px;font-weight:700;color:var(--navy)}
.review p{margin:18px auto 0;width:220px;font-size:13px;line-height:19px;color:#5a5f6a}
.stars{margin-top:20px;color:var(--star);font-size:16px;letter-spacing:3px}
.badge{background:#d7dbe4}
.site-footer{left:0;top:3683px;width:1200px;height:579px;background:var(--navy);color:var(--white)}
.foot-h{position:absolute;top:40px;font-size:16px;font-weight:700;letter-spacing:.6px}
.socials{position:absolute;left:81px;top:88px;display:flex;gap:10px}
.socials span{width:34px;height:34px;border-radius:50%;border:2px solid #6d7bab}
.address{position:absolute;left:81px;top:142px;font-size:12.5px;line-height:20px;color:#dde1ee}
.foot-links{position:absolute;left:430px;top:86px;list-style:none;font-size:12.5px;line-height:23px;color:#b9c0d8}
.foot-links li::before{content:"›";margin-right:8px}
.foot-legal{position:absolute;left:430px;top:290px;font-size:12.5px;line-height:22px;color:#b9c0d8}
.contact-form{position:absolute;left:790px;top:94px;width:294px;height:421px;border:1px solid #8d98bf;padding:12px 16px}
.field{margin-bottom:20px}
.field label{display:block;font-size:12px;font-weight:700;margin-bottom:6px}
.field span{display:block;height:38px;border:1px solid #aeb6d1}
.field.msg span{height:48px}
.form-actions{display:flex;gap:10px;margin-top:-4px;margin-left:45px}
.form-actions span{background:var(--white);color:var(--navy);font-weight:700;font-size:14px;padding:9px 12px}
.to-top{left:1156px;top:4196px;width:36px;height:36px;border-radius:50%;background:var(--white);display:flex;align-items:center;justify-content:center}
.bottom-bar{left:0;top:4262px;width:1200px;height:96px;background:var(--footer-bottom);color:#bbb;font-size:11px;line-height:18px;padding:30px 64px}
</style>
</head>
<body>

<header class="abs site-header">
  <div class="abs brand"><span class="brand-mark"></span><span class="brand-name">BRIGHT CAMPUS</span></div>
  <div class="abs util-nav">
    <span class="login">
      <svg width="12" height="12" viewBox="0 0 12 12" style="vertical-align:-1px;margin-right:6px"><circle cx="6" cy="3.5" r="3" fill="#fff"/><path d="M0 12c0-4 12-4 12 0z" fill="#fff"/></svg>Log In</span>
    <span>Contact</span><span>Support</span><span>Careers</span>
  </div>
  <nav class="abs main-nav"><span>ABOUT US</span><span>FOR HEALTH PLANS</span><span>FOR PROVIDERS</span><span>FOR PARTNERS</span><span>BLOG</span></nav>
  <div class="abs search">Search</div>
</header>

<section class="abs hero" role="img" aria-label="Smiling student carrying a backpack and books on campus">
  <h1 class="abs">Your Academic Dream is <strong>Our Impotant Choice</strong></h1>
  <p class="abs">We help our customers develop cloud migration and disaster recovery strategies.We are experts with database management, records management.</p>
  <div class="abs btn btn-green" style="left:81px;top:334px;width:247px;height:46px">Request a Demo</div>
</section>

<h2 class="abs section-title" style="top:712px">Who We are</h2>
<div class="abs title-rule" style="top:764px"></div>
<p class="abs who-text">BRIGHT CAMPUS Abu Dhabi, one of the leading and fastest growing educational consulting company based in UAE officially recognized by the National Council for Higher Learning, Intl Agent Board and QualityMark QM-100. Bright Campus was established in 2015 with an aim to provide professional consultancy services for the recruitment of quality international students to educational institutions based in UK, USA, Canada, Australia, Malaysia, Germany, Europe, Middle East and many more. Our counseling services focus on student careers making sure that they are well placed in good and reputed institutions overseas.</p>
<div class="abs btn btn-navy" style="left:491px;top:967px;width:212px;height:50px">APPLY NOW</div>

<h2 class="abs section-title" style="top:1084px">Study Destinations</h2>
<div class="abs title-rule" style="top:1156px"></div>

<div class="abs dest-card" style="left:81px;top:1214px"><div class="dest-icon" role="img" aria-label="UK landmark icon"></div><h3>Study in UK</h3><p>The department for Education &amp; Employment has given students work Part time</p><div class="btn btn-navy">Find Out More</div></div>
<div class="abs dest-card" style="left:349px;top:1214px"><div class="dest-icon" role="img" aria-label="USA landmark icon"></div><h3>Study in USA</h3><p>The department for Education &amp; Employment has given students work Part time</p><div class="btn btn-navy">Find Out More</div></div>
<div class="abs dest-card" style="left:613px;top:1214px"><div class="dest-icon" role="img" aria-label="Australia landmark icon"></div><h3>Study in Australia</h3><p>The department for Education &amp; Employment has given students work Part time</p><div class="btn btn-navy">Find Out More</div></div>
<div class="abs dest-card" style="left:877px;top:1214px"><div class="dest-icon" role="img" aria-label="New Zealand leaf icon"></div><h3>Study in New Zealand</h3><p>The department for Education &amp; Employment has given students work Part time</p><div class="btn btn-navy">Find Out More</div></div>

<div class="abs dest-card" style="left:81px;top:1557px"><div class="dest-icon" role="img" aria-label="Europe landmark icon"></div><h3>Study in Europe</h3><p>The department for Education &amp; Employment has given students work Part time</p><div class="btn btn-navy">Find Out More</div></div>
<div class="abs dest-card" style="left:349px;top:1557px"><div class="dest-icon" role="img" aria-label="Malaysia landmark icon"></div><h3>Study in Malaysia</h3><p>The department for Education &amp; Employment has given students work Part time</p><div class="btn btn-navy">Find Out More</div></div>
<div class="abs dest-card" style="left:613px;top:1557px"><div class="dest-icon" role="img" aria-label="Germany landmark icon"></div><h3>Study in Germany</h3><p>The department for Education &amp; Employment has given students work Part time</p><div class="btn btn-navy">Find Out More</div></div>
<div class="abs dest-card" style="left:877px;top:1557px"><div class="dest-icon" role="img" aria-label="China landmark icon"></div><h3>Study in Chaina</h3><p>The department for Education &amp; Employment has given students work Part time</p><div class="btn btn-navy">Find Out More</div></div>

<div class="abs why-photo" role="img" aria-label="Smiling graduate in cap with tassel"></div>
<section class="abs why-panel">
  <h2>Why Hire Us?</h2>
  <ul class="why-list">
    <li><svg width="24" height="24" viewBox="0 0 24 24"><circle cx="12" cy="12" r="10.5" fill="none" stroke="#fff" stroke-width="1.5"/><path d="M7 12.5l3.2 3 6.6-6.6" fill="none" stroke="#fff" stroke-width="1.6"/></svg><span>Experienced counselors available to help you identify the best education plan for you!</span></li>
    <li><svg width="24" height="24" viewBox="0 0 24 24"><circle cx="12" cy="12" r="10.5" fill="none" stroke="#fff" stroke-width="1.5"/><path d="M7 12.5l3.2 3 6.6-6.6" fill="none" stroke="#fff" stroke-width="1.6"/></svg><span>We officially collaborate with over 300 domestic and international accredited educational institutions to ensure you get the best quality</span></li>
    <li><svg width="24" height="24" viewBox="0 0 24 24"><circle cx="12" cy="12" r="10.5" fill="none" stroke="#fff" stroke-width="1.5"/><path d="M7 12.5l3.2 3 6.6-6.6" fill="none" stroke="#fff" stroke-width="1.6"/></svg><span>From China East to Canada West, going through USA, UK, Europe and more. We can help you decide which country is the most suitable for you based on your circumstances.</span></li>
    <li><svg width="24" height="24" viewBox="0 0 24 24"><circle cx="12" cy="12" r="10.5" fill="none" stroke="#fff" stroke-width="1.5"/><path d="M7 12.5l3.2 3 6.6-6.6" fill="none" stroke="#fff" stroke-width="1.6"/></svg><span>Registered with the National Council for Higher Learning. We are also members or multiple quality assurance and global educational associations.</span></li>
  </ul>
</section>

<h2 class="abs section-title serif-title" style="top:2600px">Apply Online</h2>
<p class="abs apply-text">Each year in the United States about $135 billion is spent in training employees — but those billions do not always improve the workplace because the skills often do not transfer to the actual job.</p>
<div class="abs btn btn-green" style="left:473px;top:2806px;width:265px;height:50px;font-size:17px">Apply Online</div>

<h2 class="abs section-title serif-title" style="top:2928px">What Our Clients Say</h2>

<div class="abs review" style="left:122px;top:3108px"><div class="avatar" style="background:#d9b49a" role="img" aria-label="Client portrait"></div><h4>Lena Hartwell</h4><div class="role">Graduate - Marlow Bay (24)</div><p>Lorem ipsum dolor sit amet, sed diam nonummy nibh euismod tincidunt ut laoreet dolore magna aliquam erat volutpat. Ut wisi enim ad</p><div class="stars">★★★★★</div></div>
<div class="abs review" style="left:456px;top:3108px"><div class="avatar" style="background:#b9a58e" role="img" aria-label="Client portrait"></div><h4>Lena Hartwell</h4><div class="role">Graduate - Marlow Bay (24)</div><p>Lorem ipsum dolor sit amet, sed diam nonummy nibh euismod tincidunt ut laoreet dolore magna aliquam erat volutpat. Ut wisi enim ad</p><div class="stars">★★★★★</div></div>
<div class="abs review" style="left:790px;top:3108px"><div class="avatar" style="background:#d8c0a6" role="img" aria-label="Client portrait"></div><h4>Lena Hartwell</h4><div class="role">Graduate - Marlow Bay (24)</div><p>Lorem ipsum dolor sit amet, sed diam nonummy nibh euismod tincidunt ut laoreet dolore magna aliquam erat volutpat. Ut wisi enim ad</p><div class="stars">★★★★★</div></div>

<div class="abs badge" role="img" aria-label="Partner badge" style="left:350px;top:3515px;width:110px;height:84px;border-radius:6px"></div>
<div class="abs badge" role="img" aria-label="Partner badge" style="left:495px;top:3509px;width:60px;height:90px;border-radius:6px"></div>
<div class="abs badge" role="img" aria-label="Partner badge" style="left:610px;top:3518px;width:72px;height:72px;border-radius:10px;background:#3a6fb8"></div>
<div class="abs badge" role="img" aria-label="Partner badge" style="left:720px;top:3530px;width:146px;height:50px;border-radius:4px;background:#3a6fb8"></div>

<footer class="abs site-footer">
  <h3 class="foot-h" style="left:81px">FOLLOW US</h3>
  <div class="socials"><span></span><span></span><span></span><span></span><span></span></div>
  <div class="address">Address:<br>Crescent Tower, Harbour Quarter,<br>Suite 31<br>3rd Floor, PO Box - 4172<br>Phone: +971 2 000 11 22<br>Mobile: 971 50 000 3344<br>+971 50 000 7788<br>+971 50 000 5566<br>Email: info@brightcampuslink.ae</div>

  <h3 class="foot-h" style="left:430px">STUDY DESTINATIONS</h3>
  <ul class="foot-links"><li>Study in UK</li><li>Study in USA</li><li>Study in Australia</li><li>Study in New Zealand</li><li>Study in Europe</li><li>Study in Germany</li><li>Study in Malaysia</li><li>Study in UAE</li></ul>
  <div class="foot-legal">Privacy Policy<br>Terms of Use</div>

  <h3 class="foot-h" style="left:778px">CONTACT US</h3>
  <div class="contact-form">
    <div class="field"><label>First Name:</label><span></span></div>
    <div class="field"><label>Last Name:</label><span></span></div>
    <div class="field"><label>Mobile:</label><span></span></div>
    <div class="field"><label>Email Address:</label><span></span></div>
    <div class="field msg"><label>Message:</label><span></span></div>
    <div class="form-actions"><span>Submit</span><span>Clear Form</span></div>
  </div>
</footer>
<div class="abs to-top"><svg width="12" height="8" viewBox="0 0 12 8"><path d="M1 7l5-5 5 5" fill="none" stroke="#1d2b5e" stroke-width="2"/></svg></div>

<div class="abs bottom-bar">© COPYRIGHT 2017 BRIGHT CAMPUS | CRESCENT TOWER, HARBOUR QUARTER, SUITE 31, 3RD FLOOR,<br>PO BOX - 4172 | PHONE: +971 02 000 1122 | EMAIL: INFO@BRIGHTCAMPUSLINK.AE</div>

</body>
</html>
```